Professional Simple Business Card Design

Design a professional business card . Simple Design.
Base colour White and purple(logo colour) which is from the logo attached. Other logo colour(orange) can be used if required.
Include dummy name and designation column which can be filled for later purpose.

Find attached Logo and other details.

```html
<!DOCTYPE html>
<html lang="en">
<head>
<meta charset="utf-8">
<title>Novathera Labs – Business Card</title>
<link rel="stylesheet" href="https://fonts.googleapis.com/css2?family=Montserrat:wght@500;600&display=swap">
<style>
  :root {
    --purple: #7b3fa6;
    --lavender: #c9b3e0;
    --orange: #f0922f;
    --white: #ffffff;
    --stage: #e9e7ec;
    --rule: #d9cce6;
  }
  * { box-sizing: border-box; margin: 0; padding: 0; }
  html, body {
    width: 1200px; height: 900px; overflow: hidden;
    background: var(--stage);
    font-family: "Montserrat", sans-serif;
  }
  .sheet {
    width: 1200px; height: 900px;
    display: flex; flex-direction: column; align-items: center; justify-content: center; gap: 50px;
  }
  .card {
    position: relative; width: 580px; height: 330px;
    background: var(--white); border-radius: 10px; overflow: hidden;
    box-shadow: 0 10px 28px rgba(40, 20, 60, 0.18);
  }
  .brand { position: absolute; display: flex; align-items: center; gap: 14px; }
  .brand-dot { width: 34px; height: 34px; border-radius: 50%; background: var(--orange); flex: none; }
  .brand-name { color: var(--purple); font-weight: 600; letter-spacing: 0.02em; line-height: 1; }
  .card-front .brand { inset: 0; justify-content: center; }
  .card-front .brand-name { font-size: 46px; }

  .card-back .brand { left: 34px; top: 62px; gap: 12px; align-items: flex-start; }
  .card-back .brand-dot { width: 24px; height: 24px; margin-top: 6px; }
  .card-back .brand-name { font-size: 34px; line-height: 1.08; }

  .holder { position: absolute; left: 34px; top: 214px; width: 200px; }
  .holder-name {
    color: var(--purple); font-size: 15px; font-weight: 600;
    padding-bottom: 6px; border-bottom: 1px solid var(--rule);
  }
  .holder-role {
    color: var(--orange); font-size: 10px; font-weight: 500;
    letter-spacing: 0.12em; text-transform: uppercase; margin-top: 6px;
  }

  .back-panel { position: absolute; inset: 0; width: 100%; height: 100%; }
  .contacts {
    position: absolute; left: 372px; top: 20px; width: 190px;
    list-style: none; display: flex; flex-direction: column; gap: 10px;
  }
  .contact { display: flex; flex-direction: column; align-items: center; gap: 5px; }
  .contact-icon {
    width: 24px; height: 24px; border-radius: 50%; background: var(--orange);
    display: flex; align-items: center; justify-content: center;
  }
  .contact-icon svg { width: 13px; height: 13px; }
  .contact-text {
    align-self: stretch; color: var(--orange); font-size: 9px; font-weight: 500; line-height: 1.4;
  }
  .contact-address .contact-text { text-transform: uppercase; font-size: 7.6px; }
  .contact-phone .contact-text { font-size: 11px; }
</style>
</head>
<body>
<main class="sheet">
  <section class="card card-front" aria-label="Card front">
    <div class="brand">
      <span class="brand-dot"></span>
      <span class="brand-name">Novathera Labs</span>
    </div>
  </section>

  <section class="card card-back" aria-label="Card back">
    <svg class="back-panel" viewBox="0 0 580 330" preserveAspectRatio="none" aria-hidden="true">
      <path d="M288,0 C290,130 336,250 376,330 L580,330 L580,0 Z" fill="var(--lavender)"/>
      <path d="M312,0 C314,130 360,250 400,330 L580,330 L580,0 Z" fill="var(--purple)"/>
    </svg>

    <div class="brand">
      <span class="brand-dot"></span>
      <span class="brand-name">Novathera<br>Labs</span>
    </div>

    <div class="holder">
      <p class="holder-name">Your Name</p>
      <p class="holder-role">Designation</p>
    </div>

    <ul class="contacts">
      <li class="contact contact-address">
        <span class="contact-icon">
          <svg viewBox="0 0 24 24"><path d="M12 2a7 7 0 0 0-7 7c0 5 7 13 7 13s7-8 7-13a7 7 0 0 0-7-7zm0 9.5A2.5 2.5 0 1 1 12 6.5a2.5 2.5 0 0 1 0 5z" fill="var(--white)"/></svg>
        </span>
        <p class="contact-text">18, Lotus Court, 3rd Floor,<br>Meadow Industrial Park, Riverside Nagar,<br>Garden Road Extension,<br>Westfield 400210</p>
      </li>
      <li class="contact contact-mail">
        <span class="contact-icon">
          <svg viewBox="0 0 24 24"><rect x="3" y="6" width="18" height="12" rx="1.5" fill="var(--white)"/><path d="M3.5 7l8.5 6 8.5-6" fill="none" stroke="var(--orange)" stroke-width="1.6"/></svg>
        </span>
        <p class="contact-text">hello@novatheralabs.com<br>novatheralabs@mail.com</p>
      </li>
      <li class="contact contact-web">
        <span class="contact-icon">
          <svg viewBox="0 0 24 24" fill="none" stroke="var(--white)" stroke-width="1.8"><circle cx="12" cy="12" r="9"/><ellipse cx="12" cy="12" rx="4" ry="9"/><path d="M3 12h18M5 7.5h14M5 16.5h14"/></svg>
        </span>
        <p class="contact-text">www.novatheralabs.com</p>
      </li>
      <li class="contact contact-phone">
        <span class="contact-icon">
          <svg viewBox="0 0 24 24"><path d="M6.6 10.8a15 15 0 0 0 6.6 6.6l2.2-2.2a1 1 0 0 1 1-.25 11.4 11.4 0 0 0 3.6.57 1 1 0 0 1 1 1V20a1 1 0 0 1-1 1A17 17 0 0 1 3 4a1 1 0 0 1 1-1h3.5a1 1 0 0 1 1 1 11.4 11.4 0 0 0 .57 3.6 1 1 0 0 1-.25 1z" fill="var(--white)"/></svg>
        </span>
        <p class="contact-text">021-55501234</p>
      </li>
    </ul>
  </section>
</main>
</body>
</html>
```